Worksheet for a seminar - wheel of wellbeing

I need a 1 page worksheet for a course I am running next week.
1. The worksheet is based is designed to tie into Dorvelle who use 4 colours per specific quadrants - Blue top left, Yellow top right, Green bottom left, Red bottom right. As this is designed to be written and to be printed, it may need to be pale colours however I am open to the correct colours with the image on top if necessary

2. The wellbeing wheel needs to be a design of it's own as it will be used in other things. I would like to have a format for the base wheel that can be changed by me (Only the title names)

3. I have provided the 2 business logo's - these down need to be too big

I hope this helps.

Corporate managers and staff - worksheet being used in a workshop

Wheel

• A professional looking wheel that can be used for other purposes. I want to be able to change the 'pie' titles. I will also require a A4 size of the wheel with blank spaces for titles
• A modern feel

```html
<!DOCTYPE html>
<html lang="en">
<head>
<meta charset="utf-8">
<title>Wheel Of Wellbeing – Worksheet</title>
<link href="https://fonts.googleapis.com/css2?family=Open+Sans:wght@300;400;600;700;800&display=swap" rel="stylesheet">
<style>
  :root{
    --teal:#4cc1a6;
    --teal-dark:#2aa58b;
    --sky:#3bb2e8;
    --sky-tab:#5cc4f0;
    --navy:#2b6fb6;
    --green:#4cae32;
    --green-dark:#2f8a2a;
    --orange:#f26a21;
    --red:#d9202f;
    --ink:#4a4a4a;
    --muted:#6b6b6b;
    --field:#ececec;
    --q-blue:#a8ddf3;
    --q-yellow:#fbf291;
    --q-green:#97d5c6;
    --q-red:#f27c96;
    --r-blue:#2aa9e1;
    --r-yellow:#f6c519;
    --r-lime:#8cc63f;
    --r-orange:#f26522;
    --r-forest:#1d7b3b;
    --r-red:#c8171f;
    --r-purple:#8e2c8f;
    --r-brown:#8d6c4c;
    --p-blue:#b9e3f7;
    --p-yellow:#fdf0bd;
    --p-lime:#dcebc6;
    --p-orange:#fbd2c0;
    --p-forest:#b8d8c5;
    --p-red:#f1c3c8;
    --p-purple:#dcc8e3;
    --p-brown:#e3d8cd;
  }
  *{box-sizing:border-box;margin:0;padding:0}
  html,body{width:755px;height:1200px;overflow:hidden;background:#fff}
  body{font-family:"Open Sans",Arial,sans-serif;color:var(--ink)}
  .sheet{position:relative;width:755px;height:1200px;overflow:hidden;background:#fff}
  .abs{position:absolute}
  .header-band{position:absolute;left:0;top:0}
  .title{position:absolute;left:0;width:755px;text-align:center;color:#fff}
  .title-main{top:18px;font-size:29px;font-weight:300;letter-spacing:.3px}
  .title-sub{top:54px;font-size:31px;font-weight:700}
  .access-tab{position:absolute;left:0;top:136px;width:158px;height:36px;background:var(--sky-tab);border-radius:0 6px 6px 0;color:#fff;font-size:25px;font-weight:400;text-align:center;line-height:36px}
  .center-text{position:absolute;text-align:center;white-space:nowrap;transform:translateX(-50%)}
  .access-q{left:177px;top:180px;font-size:17px;font-weight:700;color:var(--navy)}
  .model-title{left:177px;top:212px;font-size:22px;font-weight:600;color:var(--green)}
  .model-title sup{font-size:10px}
  .mode-label{font-size:14px;font-weight:600;color:var(--muted)}
  .cerebral{left:177px;top:248px}
  .limbic{left:177px;top:582px}
  .side-mode{position:absolute;z-index:2;font-size:14px;font-weight:600;color:var(--muted);white-space:nowrap;line-height:16px}
  .left-mode{left:36px;top:430px;transform:translate(-50%,-50%) rotate(-90deg)}
  .right-mode{left:319px;top:430px;transform:translate(-50%,-50%) rotate(90deg)}
  .goals-1{left:541px;top:164px;font-size:17px;font-weight:600;color:var(--green)}
  .goals-2{left:541px;top:189px;font-size:17px;font-weight:600;color:var(--red)}
  .date{position:absolute;left:33px;top:686px;font-size:17px;color:var(--muted)}
  .date-line{position:absolute;left:80px;top:707px;width:140px;border-bottom:1px solid #888}
  .achieved{left:572px;top:684px;font-size:23px;font-weight:700;color:var(--navy)}
  .pill{position:absolute;height:26px;border-radius:4px;color:#fff;font-size:17px;font-weight:600;text-align:center;line-height:26px;box-shadow:0 2px 0 rgba(0,0,0,.15)}
  .pill-action{left:117px;top:740px;width:151px;background:var(--green-dark)}
  .pill-reflect{left:497px;top:740px;width:152px;background:var(--r-lime)}
  .col-head{position:absolute;top:794px;font-size:15px;font-weight:600}
  .col-action{left:98px;color:#6a6fb0}
  .col-when{left:283px;color:var(--green)}
  .plan-row{position:absolute;left:20px;width:350px;height:20px;font-size:11px;color:var(--muted)}
  .plan-row .num{position:absolute;left:0;top:2px}
  .plan-row .line-action{position:absolute;left:14px;top:12px;width:183px;border-bottom:1px solid #999}
  .plan-row .line-when{position:absolute;left:232px;top:12px;width:113px;border-bottom:1px solid #999}
  .question{position:absolute;left:413px;width:319px;text-align:center;font-size:13.5px;line-height:20px;color:var(--ink)}
  .answer-field{position:absolute;left:413px;width:319px;height:32px;background:var(--field);border-radius:6px}
  .brand{position:absolute;top:1143px;font-size:21px;font-weight:700;color:var(--green);white-space:nowrap}
  .brand-left{left:30px}
  .brand-right{left:534px;color:var(--teal-dark)}
  .brand-dot{display:inline-block;width:12px;height:12px;border-radius:50%;background:currentColor;margin-right:7px;vertical-align:1px}
  .foot-band{position:absolute;left:0;top:1190px;width:755px;height:10px;background:var(--teal)}
  .foot-accent{position:absolute;left:530px;top:1190px;width:225px;height:10px;background:var(--orange)}
  .quad-text{font-size:10.5px;fill:#3d3d3d}
  .quad-tick{fill:var(--green)}
  .ring-label{font-size:10px;font-weight:700;fill:#fff;letter-spacing:.2px}
  .axis-num{font-size:9px;fill:#555}
</style>
</head>
<body>
<main class="sheet">

  <!-- Header -->
  <svg class="header-band" width="755" height="150" viewBox="0 0 755 150" aria-hidden="true">
    <path d="M0 0H755V82Q377 150 0 82Z" fill="var(--teal)"/>
  </svg>
  <h1 class="title title-main">Wheel Of Wellbeing</h1>
  <h2 class="title title-sub">A Whole Brain Approach</h2>

  <!-- Access -->
  <div class="access-tab">Access</div>
  <p class="center-text access-q">where are you now?</p>
  <p class="center-text model-title">The Dorvelle<sup>®</sup> Model</p>
  <p class="center-text mode-label cerebral">Cerebral Mode</p>
  <p class="center-text mode-label limbic">Limbic Mode</p>

  <svg class="abs quadrant-model" style="left:47px;top:300px" width="260" height="260" viewBox="-130 -130 260 260" role="img" aria-label="Four quadrant thinking model">
    <path d="M-3 -3V-121A118 118 0 0 0 -121 -3Z" fill="var(--q-blue)"/>
    <path d="M3 -3V-121A118 118 0 0 1 121 -3Z" fill="var(--q-yellow)"/>
    <path d="M-3 3V121A118 118 0 0 1 -121 3Z" fill="var(--q-green)"/>
    <path d="M3 3V121A118 118 0 0 0 121 3Z" fill="var(--q-red)"/>
    <g class="quad-text" text-anchor="end">
      <text x="-24" y="-57">Logical <tspan class="quad-tick">✓</tspan></text>
      <text x="-24" y="-43">Analytical <tspan class="quad-tick">✓</tspan></text>
      <text x="-24" y="-29">Fact Based <tspan class="quad-tick">✓</tspan></text>
      <text x="-24" y="-15">Quantitative <tspan class="quad-tick">✓</tspan></text>
      <text x="-24" y="35">Organized <tspan class="quad-tick">✓</tspan></text>
      <text x="-24" y="49">Sequential <tspan class="quad-tick">✓</tspan></text>
      <text x="-24" y="63">Planned <tspan class="quad-tick">✓</tspan></text>
      <text x="-24" y="77">Detailed <tspan class="quad-tick">✓</tspan></text>
    </g>
    <g class="quad-text">
      <text x="10" y="-57"><tspan class="quad-tick">✓</tspan> Holistic</text>
      <text x="10" y="-43"><tspan class="quad-tick">✓</tspan> Intuitive</text>
      <text x="10" y="-29"><tspan class="quad-tick">✓</tspan> Integrating</text>
      <text x="10" y="-15"><tspan class="quad-tick">✓</tspan> Sythesizing</text>
      <text x="10" y="35"><tspan style="fill:var(--red)">✓</tspan> Interpersonal</text>
      <text x="10" y="49"><tspan style="fill:var(--red)">✓</tspan> Feeling Based</text>
      <text x="10" y="63"><tspan style="fill:var(--red)">✓</tspan> Kinesthetic</text>
      <text x="10" y="77"><tspan style="fill:var(--red)">✓</tspan> Emotional</text>
    </g>
    <circle r="22" fill="#fff"/>
    <rect x="-16" y="-16" width="15" height="15" fill="var(--sky)"/>
    <rect x="1" y="-16" width="15" height="15" fill="#f7e84a"/>
    <rect x="-16" y="1" width="15" height="15" fill="var(--teal)"/>
    <rect x="1" y="1" width="15" height="15" fill="#ee4d6e"/>
    <g font-size="10" font-weight="700" fill="#fff" text-anchor="middle">
      <text x="-8.5" y="-4.5">A</text><text x="8.5" y="-4.5" fill="#777">D</text>
      <text x="-8.5" y="12.5">B</text><text x="8.5" y="12.5">C</text>
    </g>
  </svg>

  <!-- Outcomes wheel -->
  <p class="center-text goals-1">Outcomes&nbsp; Goals</p>
  <p class="center-text goals-2">where do you want to be?</p>

  <svg class="abs wellbeing-wheel" style="left:347px;top:251px" width="388" height="388" viewBox="-194 -194 388 388" role="img" aria-label="Wheel of wellbeing with eight life areas scored 0 to 10">
    <defs>
      <path id="arc-physical" d="M0 -175A175 175 0 0 1 123.74 -123.74"/>
      <path id="arc-emotional" d="M123.74 -123.74A175 175 0 0 1 175 0"/>
      <path id="arc-spiritual" d="M175 0A175 175 0 0 1 123.74 123.74"/>
      <path id="arc-love" d="M123.74 123.74A175 175 0 0 1 0 175"/>
      <path id="arc-family" d="M0 175A175 175 0 0 1 -123.74 123.74"/>
      <path id="arc-social" d="M-123.74 123.74A175 175 0 0 1 -175 0"/>
      <path id="arc-growth" d="M-175 0A175 175 0 0 1 -123.74 -123.74"/>
      <path id="arc-career" d="M-123.74 -123.74A175 175 0 0 1 0 -175"/>
      <g id="axis">
        <line x1="0" y1="0" x2="0" y2="-152" stroke="#5a5a5a" stroke-width=".8"/>
        <g stroke="#5a5a5a" stroke-width=".8">
          <line x1="-3" y1="-15" x2="3" y2="-15"/><line x1="-3" y1="-30" x2="3" y2="-30"/>
          <line x1="-3" y1="-45" x2="3" y2="-45"/><line x1="-3" y1="-60" x2="3" y2="-60"/>
          <line x1="-5" y1="-75" x2="5" y2="-75"/><line x1="-3" y1="-90" x2="3" y2="-90"/>
          <line x1="-3" y1="-105" x2="3" y2="-105"/><line x1="-3" y1="-120" x2="3" y2="-120"/>
          <line x1="-3" y1="-135" x2="3" y2="-135"/><line x1="-5" y1="-150" x2="5" y2="-150"/>
        </g>
        <text class="axis-num" x="5" y="-72">5</text>
        <text class="axis-num" x="5" y="-140">10</text>
      </g>
    </defs>
    <!-- inner segments -->
    <g transform="rotate(-90)" fill="none" stroke-width="166">
      <circle r="83" stroke="var(--p-yellow)" stroke-dasharray="65.19 456.33"/>
      <circle r="83" stroke="var(--p-lime)" stroke-dasharray="65.19 456.33" stroke-dashoffset="-65.19"/>
      <circle r="83" stroke="var(--p-orange)" stroke-dasharray="65.19 456.33" stroke-dashoffset="-130.38"/>
      <circle r="83" stroke="var(--p-forest)" stroke-dasharray="65.19 456.33" stroke-dashoffset="-195.57"/>
      <circle r="83" stroke="var(--p-red)" stroke-dasharray="65.19 456.33" stroke-dashoffset="-260.76"/>
      <circle r="83" stroke="var(--p-purple)" stroke-dasharray="65.19 456.33" stroke-dashoffset="-325.95"/>
      <circle r="83" stroke="var(--p-brown)" stroke-dasharray="65.19 456.33" stroke-dashoffset="-391.14"/>
      <circle r="83" stroke="var(--p-blue)" stroke-dasharray="65.19 456.33" stroke-dashoffset="-456.33"/>
    </g>
    <!-- outer ring -->
    <g transform="rotate(-90)" fill="none" stroke-width="22">
      <circle r="179" stroke="var(--r-yellow)" stroke-dasharray="140.6 984.1"/>
      <circle r="179" stroke="var(--r-lime)" stroke-dasharray="140.6 984.1" stroke-dashoffset="-140.6"/>
      <circle r="179" stroke="var(--r-orange)" stroke-dasharray="140.6 984.1" stroke-dashoffset="-281.2"/>
      <circle r="179" stroke="var(--r-forest)" stroke-dasharray="140.6 984.1" stroke-dashoffset="-421.8"/>
      <circle r="179" stroke="var(--r-red)" stroke-dasharray="140.6 984.1" stroke-dashoffset="-562.4"/>
      <circle r="179" stroke="var(--r-purple)" stroke-dasharray="140.6 984.1" stroke-dashoffset="-703"/>
      <circle r="179" stroke="var(--r-brown)" stroke-dasharray="140.6 984.1" stroke-dashoffset="-843.6"/>
      <circle r="179" stroke="var(--r-blue)" stroke-dasharray="140.6 984.1" stroke-dashoffset="-984.2"/>
    </g>
    <!-- dividers -->
    <g stroke="#fff" stroke-width="2.5">
      <line x1="0" y1="0" x2="0" y2="-191"/>
      <line x1="0" y1="0" x2="135" y2="-135"/>
      <line x1="0" y1="0" x2="191" y2="0"/>
      <line x1="0" y1="0" x2="135" y2="135"/>
      <line x1="0" y1="0" x2="0" y2="191"/>
      <line x1="0" y1="0" x2="-135" y2="135"/>
      <line x1="0" y1="0" x2="-191" y2="0"/>
      <line x1="0" y1="0" x2="-135" y2="-135"/>
    </g>
    <circle r="167" fill="none" stroke="#fff" stroke-width="2"/>
    <!-- scales -->
    <use href="#axis" transform="rotate(22.5)"/>
    <use href="#axis" transform="rotate(67.5)"/>
    <use href="#axis" transform="rotate(112.5)"/>
    <use href="#axis" transform="rotate(157.5)"/>
    <use href="#axis" transform="rotate(202.5)"/>
    <use href="#axis" transform="rotate(247.5)"/>
    <use href="#axis" transform="rotate(292.5)"/>
    <use href="#axis" transform="rotate(337.5)"/>
    <!-- area labels -->
    <g class="ring-label" text-anchor="middle">
      <text><textPath href="#arc-physical" startOffset="50%">Physical Health</textPath></text>
      <text><textPath href="#arc-emotional" startOffset="50%">Emotional Health</textPath></text>
      <text><textPath href="#arc-spiritual" startOffset="50%">Spiritual</textPath></text>
      <text><textPath href="#arc-love" startOffset="50%">Love / Relationship</textPath></text>
      <text><textPath href="#arc-family" startOffset="50%">Family</textPath></text>
      <text><textPath href="#arc-social" startOffset="50%">Social</textPath></text>
      <text><textPath href="#arc-growth" startOffset="50%">Personal Growth</textPath></text>
      <text><textPath href="#arc-career" startOffset="50%">Business Career Study</textPath></text>
    </g>
  </svg>

  <p class="side-mode left-mode">Left Mode</p>
  <p class="side-mode right-mode">Right Mode</p>

  <!-- Action plan -->
  <p class="date">Date:</p>
  <div class="date-line"></div>
  <p class="center-text achieved">Date Achived By:</p>

  <div class="pill pill-action">Action Plan</div>
  <div class="pill pill-reflect">Reflect</div>

  <p class="col-head col-action">Action</p>
  <p class="col-head col-when">When</p>

  <div class="plan-row" style="top:832px"><span class="num">1.</span><span class="line-action"></span><span class="line-when"></span></div>
  <div class="plan-row" style="top:912px"><span class="num">2.</span><span class="line-action"></span><span class="line-when"></span></div>
  <div class="plan-row" style="top:992px"><span class="num">3.</span><span class="line-action"></span><span class="line-when"></span></div>
  <div class="plan-row" style="top:1072px"><span class="num">4.</span><span class="line-action"></span><span class="line-when"></span></div>

  <!-- Reflect -->
  <p class="question" style="top:782px">Are there any surprises in your wheel?</p>
  <div class="answer-field" style="top:808px"></div>
  <p class="question" style="top:852px">What well-being gaps stand out as<br>being most important</p>
  <div class="answer-field" style="top:900px"></div>
  <p class="question" style="top:944px">How do you feel about it</p>
  <div class="answer-field" style="top:970px"></div>
  <p class="question" style="top:1014px">How might this affect your<br>home life / work life</p>
  <div class="answer-field" style="top:1062px"></div>

  <!-- Brands -->
  <p class="brand brand-left"><span class="brand-dot"></span>Rootline Partners</p>
  <p class="brand brand-right"><span class="brand-dot"></span>Calmfield Works</p>

  <div class="foot-band"></div>
  <div class="foot-accent"></div>
</main>
</body>
</html>
```